Harborline Energy - needs a business card

Harborline Energy is a U.S. based diesel sourcing and distribution company that supports American oil & gas fields through providing quality product and consistent services.

Target Market(s)

Oil and Gas

Contact Information for Business Card

The background of the card must be white to ensure the logo pops.

Font styles to use
Serif
Sans Serif

Colors

Designer to choose colors to be used in the design.

Requirements
Must have
• Front of Card: Tag line: Harborline Energy, Powering America's Oil & Gas fields.
• Not sure if you guys do this part but just in case...
• Dale Menschow
• Owner/CEO
• C:555.318.4076
• E:Dmenschow@harborlineenergy.example
• W:Harborlineenergy.example
• Locations: Servicing the Powder River, DJ basin and Bakken formations.
• Back of Card: " Frac fueling is what we do. We understand how important diesel fuel is to your operation, which is why our main service line is Frac fueling. We assure our supply and stand by our service"

```html
<!DOCTYPE html>
<html lang="en">
<head>
<meta charset="UTF-8">
<title>Harborline Energy — Business Card</title>
<link rel="stylesheet" href="https://fonts.googleapis.com/css2?family=Montserrat:ital,wght@0,400;0,500;0,700;0,800;1,400&display=swap">
<style>
  :root {
    --navy: #1f3170;
    --red: #c1272d;
    --ink: #3a3a3a;
    --muted: #6b6b6b;
    --card: #ffffff;
    --backdrop: #d9dadb;
  }
  * { box-sizing: border-box; margin: 0; padding: 0; }
  html, body { width: 1200px; height: 1200px; overflow: hidden; }
  body {
    background: var(--backdrop);
    font-family: "Montserrat", Arial, sans-serif;
    display: flex;
    flex-direction: column;
    align-items: center;
    justify-content: center;
    gap: 60px;
  }
  .card {
    position: relative;
    width: 840px;
    height: 480px;
    background: var(--card);
    box-shadow: 0 6px 18px rgba(0,0,0,0.12);
    overflow: hidden;
  }
  .brand {
    display: flex;
    align-items: center;
    gap: 16px;
  }
  .brand-dot {
    width: 54px; height: 54px;
    border-radius: 50%;
    background: var(--navy);
    flex: none;
  }
  .brand-name {
    font-weight: 800;
    font-size: 34px;
    letter-spacing: 0.5px;
    color: var(--navy);
    line-height: 1.05;
  }

  /* Front */
  .card-front .content {
    position: absolute;
    left: 80px; top: 64px;
  }
  .person { margin-top: 44px; }
  .person-name {
    font-weight: 700;
    font-size: 30px;
    letter-spacing: 1.5px;
    text-transform: uppercase;
    color: var(--navy);
  }
  .person-name .surname { color: var(--red); }
  .person-title {
    font-size: 20px;
    color: var(--muted);
    letter-spacing: 1.5px;
    margin-top: 4px;
  }
  .contact-list { list-style: none; margin-top: 24px; }
  .contact-item {
    display: flex;
    align-items: flex-start;
    gap: 14px;
    font-size: 17px;
    color: var(--ink);
    letter-spacing: 0.5px;
    line-height: 1.5;
    margin-bottom: 5px;
  }
  .contact-icon { width: 18px; height: 18px; flex: none; margin-top: 4px; }

  /* Back */
  .corner { position: absolute; top: 0; left: 0; }
  .card-back .content {
    position: absolute;
    left: 200px; right: 170px; top: 110px;
    display: flex;
    flex-direction: column;
    align-items: center;
  }
  .quote {
    margin-top: 44px;
    font-style: italic;
    font-size: 18px;
    line-height: 1.6;
    color: var(--ink);
    text-align: center;
  }
</style>
</head>
<body>

<section class="card card-front" aria-label="Business card front">
  <div class="content">
    <div class="brand">
      <span class="brand-dot"></span>
      <span class="brand-name">Harborline Energy</span>
    </div>
    <div class="person">
      <h1 class="person-name">Dale <span class="surname">Menschow</span></h1>
      <p class="person-title">Owner/CEO</p>
    </div>
    <ul class="contact-list">
      <li class="contact-item">
        <svg class="contact-icon" viewBox="0 0 24 24"><path fill="#3a3a3a" d="M6.6 10.8a15.1 15.1 0 0 0 6.6 6.6l2.2-2.2a1 1 0 0 1 1-.25 11.4 11.4 0 0 0 3.6.57 1 1 0 0 1 1 1V20a1 1 0 0 1-1 1A17 17 0 0 1 3 4a1 1 0 0 1 1-1h3.5a1 1 0 0 1 1 1c0 1.25.2 2.45.57 3.57a1 1 0 0 1-.25 1z"/></svg>
        <span>555.318.4076</span>
      </li>
      <li class="contact-item">
        <svg class="contact-icon" viewBox="0 0 24 24"><rect x="2.5" y="5" width="19" height="14" fill="none" stroke="#3a3a3a" stroke-width="2"/><path d="M3 6l9 7 9-7" fill="none" stroke="#3a3a3a" stroke-width="2"/></svg>
        <span>Dmenschow@harborlineenergy.example</span>
      </li>
      <li class="contact-item">
        <svg class="contact-icon" viewBox="0 0 24 24"><circle cx="12" cy="12" r="9.5" fill="none" stroke="#3a3a3a" stroke-width="2"/><ellipse cx="12" cy="12" rx="4" ry="9.5" fill="none" stroke="#3a3a3a" stroke-width="1.6"/><path d="M2.5 12h19M4 7h16M4 17h16" stroke="#3a3a3a" stroke-width="1.4"/></svg>
        <span>Harborlineenergy.example</span>
      </li>
      <li class="contact-item">
        <svg class="contact-icon" viewBox="0 0 24 24"><path fill="#3a3a3a" d="M12 2a7 7 0 0 0-7 7c0 5.2 7 13 7 13s7-7.8 7-13a7 7 0 0 0-7-7zm0 9.5A2.5 2.5 0 1 1 12 6.5a2.5 2.5 0 0 1 0 5z"/></svg>
        <span>Servicing the Powder River, DJ<br>basin and Bakken formations</span>
      </li>
    </ul>
  </div>
</section>

<section class="card card-back" aria-label="Business card back">
  <svg class="corner" width="840" height="480" viewBox="0 0 840 480" aria-hidden="true">
    <polygon points="0,0 170,0 0,340" fill="var(--navy)"/>
    <polygon points="840,140 840,480 670,480" fill="var(--red)"/>
  </svg>
  <div class="content">
    <div class="brand">
      <span class="brand-dot"></span>
      <span class="brand-name">Harborline Energy</span>
    </div>
    <p class="quote">“ Frac fueling is what we do. We understand how important diesel fuel is to your operation, which is why our main service line is Frac fueling. We assure our supply and stand by our service”</p>
  </div>
</section>

</body>
</html>
```